Calloway needs a modernized design

We would like a modern update (that can be responsive) to our existing website. Attached are the two existing pages we would like new concepts of - our home page and a page about one of our locations.

Calloway is provides executive offices and virtual office services. Startups, law firms, and financial services are our primary clients. We would like a professional, clean design, leaning towards minimalist. We intend to greatly reduce/eliminate the long paragraphs of text.

Industry/Entity Type

Business Service

Number of Pages Required

2 page

Requirements
Must have
• A design that can be responsive
Nice to have
• Large image(s) on home page that rotate.

```html
<!DOCTYPE html>
<html lang="en">
<head>
<meta charset="utf-8">
<title>Calloway Business Centers</title>
<link href="https://fonts.googleapis.com/css2?family=Roboto:wght@400;500;700&display=swap" rel="stylesheet">
<style>
:root{
  --navy:#1d3c7c;
  --navy-dark:#183468;
  --slate:#9eabd0;
  --slate-footer:#8d9bc8;
  --panel:#f0f0f0;
  --ink:#222;
  --muted:#555;
  --rule:#dedede;
  --white:#fff;
}
*{box-sizing:border-box;margin:0;padding:0}
html,body{width:1200px;height:2757px;overflow:hidden}
body{position:relative;background:var(--white);font-family:"Roboto",Arial,sans-serif;color:var(--ink)}
.abs{position:absolute}
/* header */
.brand{left:130px;top:20px;display:flex;align-items:center;gap:10px}
.brand-dot{width:54px;height:54px;border-radius:50%;background:var(--navy)}
.brand-name{font-size:26px;font-weight:500;color:var(--navy);line-height:1}
.brand-name small{display:block;font-size:11px;letter-spacing:1px;margin-top:4px}
.office{top:20px;font-size:11px;line-height:20px;color:var(--ink)}
.office b{font-weight:700;display:block;font-size:11px}
.office.houston{border-left:1px solid #999;padding-left:10px}
.callbar{left:830px;top:20px;font-size:11px;display:flex;align-items:center;gap:4px}
.social{width:17px;height:17px;background:var(--navy);display:inline-block;border-radius:2px}
.search{left:770px;top:42px;width:300px;height:28px;border-bottom:1px solid #ccc}
.search svg{position:absolute;right:0;top:4px}
/* nav */
.nav{left:0;top:93px;width:1200px;height:51px;background:var(--navy)}
.nav a{position:absolute;top:17px;color:var(--white);font-size:15px;font-weight:500;text-decoration:none}
.subnav{left:132px;top:134px;width:934px;height:68px;background:var(--slate);z-index:2}
.subnav span{position:absolute;top:17px;color:var(--white);font-size:13px;line-height:18px;text-transform:uppercase}
.hero{left:0;top:143px;width:1200px;height:372px;background:linear-gradient(180deg,#8a8a8c 0%,#d8b797 45%,#b98a63 62%,#3e5a73 80%,#1d3148 100%)}
/* services */
.service{top:570px;width:221px;height:395px;background:var(--panel)}
.service h3{height:50px;background:var(--navy);color:var(--white);font-size:22px;font-weight:500;padding:12px 14px;display:flex;justify-content:space-between;align-items:center}
.service h3 i{width:22px;height:22px;border-radius:50%;background:var(--white);display:block}
.service ul{list-style:none;padding:22px 14px 0 20px}
.service li{font-size:13px;line-height:19px;padding-left:25px;position:relative;margin-bottom:20px}
.service li::before{content:"›";position:absolute;left:0;top:-1px;font-size:15px}
.rule{left:132px;width:938px;height:1px;background:var(--rule)}
/* sections */
.tag{background:var(--navy);color:var(--white);font-weight:500;padding:0 8px;display:inline-block;line-height:1.1}
.about-title{left:132px;top:1073px;font-size:38px;display:flex;gap:14px;align-items:center}
.about-title .tag{font-size:36px}
.copy{font-size:13px;line-height:19px;color:var(--muted)}
.copy p{margin-bottom:18px}
.photo{background:linear-gradient(135deg,#c9d0d9,#6f7886)}
.section-tag{left:132px;font-size:25px}
.member{top:1510px;width:223px}
.member .photo{height:221px;background:linear-gradient(135deg,#b9c3c8,#5d6e78)}
.member h4{font-size:17px;font-weight:700;margin-top:20px}
.member p{font-size:11px;color:var(--muted);margin-top:14px}
.quote{top:1895px;width:223px;height:303px;border:1px solid #ddd;border-radius:3px;padding:14px 14px;font-size:13px;line-height:19px;color:var(--muted)}
.client{top:2215px;display:flex;gap:12px;font-size:13px;line-height:20px}
.client .avatar{width:46px;height:46px;background:linear-gradient(135deg,#b49480,#5a4a3e)}
.client b{font-weight:700;color:var(--ink);display:block}
/* footer */
.footer-side{left:0;top:2334px;width:432px;height:423px;background:var(--slate-footer)}
.footer-main{left:432px;top:2375px;width:768px;height:382px;background:var(--navy)}
.footer-brand{left:178px;top:2380px;display:flex;align-items:center;gap:8px}
.footer-brand .brand-dot{width:44px;height:44px;background:var(--white)}
.footer-brand .brand-name{color:var(--white);font-size:22px}
.contact{left:172px;font-size:12px;color:var(--white);display:flex;gap:4px;align-items:center}
.fcol{top:2420px;width:160px;color:var(--white)}
.fcol h5{font-size:16px;font-weight:500;margin-bottom:26px}
.fcol li{list-style:none;font-size:11px;line-height:35px;padding-left:18px;position:relative}
.fcol li::before{content:"›";position:absolute;left:0}
</style>
</head>
<body>

<header>
  <div class="abs brand"><span class="brand-dot"></span><span class="brand-name">CALLOWAY<small>BUSINESS CENTERS</small></span></div>
  <div class="abs office" style="left:450px"><b>OFFICE DALLAS</b>⌂ Harlow Street 118<br>☏ 214.555.0142</div>
  <div class="abs office houston" style="left:598px"><b>OFFICE HOUSTON</b>⌂ Harlow Street 118<br>☏ 713.555.0187</div>
  <div class="abs callbar">Call us now ☏ 713.555.0187 <span class="social"></span><span class="social"></span><span class="social"></span><span class="social"></span></div>
  <div class="abs search"><svg width="18" height="18" viewBox="0 0 18 18"><circle cx="7" cy="7" r="5.5" fill="none" stroke="#111" stroke-width="2.4"/><line x1="11" y1="11" x2="16.5" y2="16.5" stroke="#111" stroke-width="2.6"/></svg></div>
</header>

<nav class="abs nav">
  <a style="left:150px">HOME</a><a style="left:232px">PROPERTIES</a><a style="left:358px">VIRTUAL TOURS</a><a style="left:509px">PHOTOS</a><a style="left:606px">BROKER REFERRALS</a><a style="left:788px">CONTACT US</a>
</nav>
<div class="abs subnav">
  <span style="left:87px">Executive<br>Office Suites</span><span style="left:210px">Meeting<br>Conference Rooms</span><span style="left:377px">On-Demand<br>Training Rooms</span><span style="left:520px">Virtual<br>Office Solutions</span><span style="left:671px">Video<br>Conference Solutions</span>
</div>
<div class="abs hero" role="img" aria-label="Sailing yacht on the sea at sunset with a small island behind"></div>

<section>
  <div class="abs service" style="left:132px"><h3>INVESTMENTS<i></i></h3><ul><li>Cras ornare tristique elit.</li><li>Vivamus vestibulum nulla nec.</li><li>Praesent placerat risus quis.</li><li>Fusce pellentesque suscipit.</li><li>Cras ornare tristique elit.</li><li>Vivamus vestibulum nulla nec.</li></ul></div>
  <div class="abs service" style="left:371px"><h3>TRAINING<i></i></h3><ul><li>Cras ornare tristique elit.</li><li>Vivamus vestibulum nulla nec.</li><li>Praesent placerat risus quis.</li><li>Fusce pellentesque suscipit.</li><li>Cras ornare tristique elit.</li><li>Vivamus vestibulum nulla nec.</li></ul></div>
  <div class="abs service" style="left:610px"><h3>SOLUTIONS<i></i></h3><ul><li>Cras ornare tristique elit.</li><li>Vivamus vestibulum nulla nec.</li><li>Praesent placerat risus quis.</li><li>Fusce pellentesque suscipit.</li><li>Cras ornare tristique elit.</li><li>Vivamus vestibulum nulla nec.</li></ul></div>
  <div class="abs service" style="left:849px"><h3>CONSULTING<i></i></h3><ul><li>Cras ornare tristique elit.</li><li>Vivamus vestibulum nulla nec.</li><li>Praesent placerat risus quis.</li><li>Fusce pellentesque suscipit.</li><li>Cras ornare tristique elit.</li><li>Vivamus vestibulum nulla nec.</li></ul></div>
</section>

<div class="abs rule" style="top:1024px"></div>

<section>
  <h2 class="abs about-title"><span class="tag">ABOUT</span><span style="font-weight:400">| Meet our agency and our insurance</span></h2>
  <div class="abs copy" style="left:132px;top:1165px;width:448px">
    <p>Lorem ipsum dolor sit amet, consetetur sadipscing elitr, sed diam nonumy eirmod tempor invidunt ut labore et dolore magna aliquyam erat, sed diam voluptua. At vero eos et accusam et justo duo dolores et ea rebum.</p>
    <p>Stet clita kasd gubergren, no sea takimata sanctus est Lorem ipsum dolor sit amet. Lorem ipsum dolor sit amet, consetetur sadipscing elitr, sed diam nonumy eirmod tempor invidunt ut labore et dolore magna aliquyam erat, sed diam voluptua. At vero eos et accusam et justo duo dolores et ea rebum. Stet clita kasd gubergren, no sea takimata sanctus est Lorem ipsum dolor sit amet.</p>
  </div>
  <div class="abs photo" style="left:610px;top:1167px;width:147px;height:98px" role="img" aria-label="Business people in a meeting"></div>
  <div class="abs photo" style="left:767px;top:1167px;width:147px;height:98px" role="img" aria-label="Colleagues working at a laptop"></div>
  <div class="abs photo" style="left:923px;top:1167px;width:147px;height:98px" role="img" aria-label="Team around a conference table"></div>
  <div class="abs photo" style="left:610px;top:1274px;width:147px;height:98px" role="img" aria-label="Businessman by office windows"></div>
  <div class="abs photo" style="left:767px;top:1274px;width:147px;height:98px" role="img" aria-label="Open plan office workspace"></div>
  <div class="abs photo" style="left:923px;top:1274px;width:147px;height:98px" role="img" aria-label="Group of business staff standing"></div>
</section>

<div class="abs rule" style="top:1458px"></div>

<section>
  <h2 class="abs section-tag tag" style="top:1510px">OUR TEAM</h2>
  <div class="abs copy" style="left:132px;top:1550px;width:220px">
    <p>At vero eos et accusam et justo duo dolores et ea rebum. Stet clita kasd gubergren, no sea takimata sanctus est.</p>
    <p>Stet clita kasd gubergren, no sea takimata sanctus est Lorem ipsum dolor sit amet. Lorem ipsum dolor sit amet, consetetur sadipscing elitr</p>
  </div>
  <div class="abs member" style="left:371px"><div class="photo" role="img" aria-label="Portrait of team member seated in an office chair"></div><h4>Evan Hale</h4><p>Management</p></div>
  <div class="abs member" style="left:609px"><div class="photo" role="img" aria-label="Portrait of team member seated in an office"></div><h4>Theo Marsh</h4><p>Consulting</p></div>
  <div class="abs member" style="left:847px"><div class="photo" role="img" aria-label="Portrait of team member at a desk"></div><h4>Owen Reed</h4><p>Consulting</p></div>
</section>

<div class="abs rule" style="top:1843px"></div>

<section>
  <h2 class="abs section-tag tag" style="top:1895px">OUR CLIENTS</h2>
  <div class="abs copy" style="left:132px;top:1935px;width:220px">
    <p>At vero eos et accusam et justo duo dolores et ea rebum. Stet clita kasd gubergren, no sea takimata sanctus est.</p>
    <p>Stet clita kasd gubergren, no sea takimata sanctus est Lorem ipsum dolor sit amet. Lorem ipsum dolor sit amet, consetetur sadipscing elitr</p>
  </div>
  <div class="abs quote" style="left:371px">Lorem ipsum dolor sit amet, consetetur sadipscing elitr, sed diam nonumyeirm ipsum dolor sit amet, consetetur sadipscing elitr, sed diam nonumy eirmod tempor invidunt ut labore et dolore magna aliquyam erat, sed diam voluptua. At vero eos et accusam et justo duo dolores et ea rebum. Stet clita kasd gubergren, no sea takimata sanctus est Lorem ipsum dolor sit amet.</div>
  <div class="abs quote" style="left:609px">Lorem ipsum dolor sit amet, consetetur sadipscing elitr, sed diam nonumyeirm ipsum dolor sit amet, consetetur sadipscing elitr, sed diam nonumy eirmod tempor invidunt ut labore et dolore magna aliquyam erat, sed diam voluptua. At vero eos et accusam et justo duo dolores et ea rebum. Stet clita kasd gubergren, no sea takimata sanctus est Lorem ipsum dolor sit amet.</div>
  <div class="abs quote" style="left:847px">Lorem ipsum dolor sit amet, consetetur sadipscing elitr, sed diam nonumyeirm ipsum dolor sit amet, consetetur sadipscing elitr, sed diam nonumy eirmod tempor invidunt ut labore et dolore magna aliquyam erat, sed diam voluptua. At vero eos et accusam et justo duo dolores et ea rebum. Stet clita kasd gubergren, no sea takimata sanctus est Lorem ipsum dolor sit amet.</div>
  <div class="abs client" style="left:371px"><div class="avatar" role="img" aria-label="Client portrait"></div><div><b>Dana Cole</b>Cole Energy</div></div>
  <div class="abs client" style="left:609px"><div class="avatar" role="img" aria-label="Client portrait"></div><div><b>Rafe Orlan</b>Florida</div></div>
  <div class="abs client" style="left:847px"><div class="avatar" role="img" aria-label="Client portrait"></div><div><b>Milo Grant</b>Grant Partners, New York</div></div>
</section>

<footer>
  <div class="abs footer-side"></div>
  <div class="abs footer-main"></div>
  <div class="abs footer-brand"><span class="brand-dot"></span><span class="brand-name">CALLOWAY</span></div>
  <div class="abs contact" style="top:2481px">⌂ 4210 Westbrook Avenue</div>
  <div class="abs contact" style="top:2519px">☏ 1.800.555.0199</div>
  <div class="abs contact" style="top:2558px">☎ 713.555.0187</div>
  <div class="abs fcol" style="left:450px"><h5>About Us</h5><ul><li>Testimonials</li><li>FAQs</li><li>Careers</li><li>Furniture</li><li>Specials</li><li>Site Map</li><li>Privacy</li></ul></div>
  <div class="abs fcol" style="left:608px"><h5>Recent Posts</h5><ul><li>This is a Gallery Post</li><li>Gallery Post</li><li>Featured Image Post</li><li>Image Post</li><li>Link Post</li></ul></div>
  <div class="abs fcol" style="left:766px"><h5>About Us</h5><ul><li>Testimonials</li><li>FAQs</li><li>Careers</li><li>Furniture</li><li>Specials</li><li>Site Map</li><li>Privacy</li></ul></div>
  <div class="abs fcol" style="left:923px"><h5>About Us</h5><ul><li>Testimonials</li><li>FAQs</li><li>Careers</li><li>Furniture</li><li>Specials</li><li>Site Map</li><li>Privacy</li></ul></div>
</footer>

</body>
</html>
```